Banner poster with different motifs

I'm looking for 5 banners and posters in A1 format in the same design, or the similarity must be recognizable...
Kept quite simple with different titles.

1 ballet
2 Contemporary Dance
3 high heels
4 Salsa & Bachata & Zouk
5 Hip Hop

Modern bright colors
it is for the entrance so that the students see here is a dance school

The text may also be included in the image
The photos are for guidance only; some are our own, some are purchased. However, we are permitted to use them, including our logo, of course.

```html
<!DOCTYPE html>
<html lang="en">
<head>
<meta charset="utf-8">
<title>Dance Poster</title>
<link href="https://fonts.googleapis.com/css2?family=Oswald:wght@600&family=Josefin+Sans:wght@300;400&family=Open+Sans:wght@700&display=swap" rel="stylesheet">
<style>
  :root {
    --stage: #e6e6e6;
    --paper: #ffffff;
    --ink: #1c1c1c;
    --brand-ink: #2a2a2a;
    --bronze-light: #a9774a;
    --bronze-dark: #5a3418;
    --glow-orange: #f28a2e;
    --glow-peach: #f7d2b0;
    --glow-pink: #ec5aa6;
    --photo-skin: #ead9cc;
    --photo-cloth: #f4ece6;
    --photo-navy: #5f6078;
  }
  * { margin: 0; padding: 0; box-sizing: border-box; }
  html, body {
    width: 1200px; height: 1200px; overflow: hidden;
    background: var(--stage);
  }
  .poster {
    position: absolute; left: 0; top: 176px;
    width: 1200px; height: 847px; overflow: hidden;
    background:
      radial-gradient(circle at 110px 115px, var(--glow-orange) 0, rgba(242,138,46,.55) 70px, rgba(247,210,176,.35) 190px, rgba(255,255,255,0) 320px),
      radial-gradient(ellipse 300px 260px at 1120px 720px, var(--glow-pink) 0, rgba(236,90,166,.45) 120px, rgba(255,255,255,0) 300px),
      radial-gradient(ellipse 520px 300px at 900px 60px, rgba(247,210,176,.55), rgba(255,255,255,0) 70%),
      linear-gradient(90deg, rgba(247,210,176,.35), var(--paper) 30%, var(--paper) 60%, rgba(247,210,176,.4));
  }
  .photo-ensemble {
    position: absolute; left: 624px; top: 260px; width: 576px; height: 512px;
    background:
      radial-gradient(ellipse 160px 220px at 160px 300px, rgba(95,96,120,.55), rgba(95,96,120,0) 70%),
      radial-gradient(ellipse 200px 240px at 400px 260px, rgba(234,217,204,.8), rgba(234,217,204,0) 70%),
      radial-gradient(ellipse 260px 200px at 300px 200px, rgba(236,190,200,.45), rgba(255,255,255,0) 75%);
    opacity: .85;
  }
  .photo-ballerina {
    position: absolute; left: 300px; top: 82px; width: 320px; height: 742px;
    background:
      radial-gradient(ellipse 110px 70px at 160px 445px, var(--photo-cloth), rgba(244,236,230,0) 80%),
      linear-gradient(180deg, rgba(234,217,204,0) 0, rgba(234,217,204,.9) 12%, var(--photo-skin) 50%, rgba(234,217,204,.6) 90%, rgba(234,217,204,0));
    border-radius: 140px 140px 40px 40px / 300px 300px 40px 40px;
    opacity: .9;
  }
  .floor {
    position: absolute; left: 0; right: 0; bottom: 0; height: 70px;
    background: linear-gradient(180deg, rgba(255,255,255,0), rgba(225,220,218,.45));
  }
  .headline {
    position: absolute; left: 0; top: 0; width: 1200px; height: 847px;
  }
  .headline text {
    font-family: 'Oswald', sans-serif; font-weight: 600;
  }
  .brand {
    position: absolute; left: 820px; top: 72px; width: 310px;
    text-align: center; color: var(--brand-ink);
  }
  .brand-mark {
    width: 98px; height: 98px; margin: 0 auto 16px;
    border: 2px solid var(--brand-ink); border-radius: 50%;
  }
  .brand-name {
    font-family: 'Josefin Sans', sans-serif; font-weight: 300;
    font-size: 40px; letter-spacing: 3px; line-height: 1;
  }
  .brand-tagline {
    font-family: 'Josefin Sans', sans-serif; font-weight: 300;
    font-size: 14px; letter-spacing: 3.4px; margin-top: 8px;
  }
  .class-list {
    position: absolute; left: 664px; top: 567px; list-style: none;
    font-family: 'Open Sans', sans-serif; font-weight: 700;
    font-size: 29px; color: var(--ink); line-height: 39.5px;
  }
  .class-list li { display: flex; align-items: center; }
  .class-list svg { width: 14px; height: 18px; margin-right: 13px; flex: none; }
</style>
</head>
<body>
  <main class="poster">
    <div class="photo-ensemble" role="img" aria-label="Soft-focus photo of contemporary dancers in motion"></div>
    <div class="photo-ballerina" role="img" aria-label="Photo of a ballerina en pointe in a white tutu, arm raised"></div>
    <div class="floor"></div>

    <svg class="headline" viewBox="0 0 1200 847" aria-label="DANCE">
      <defs>
        <linearGradient id="bronze" x1="0" y1="0" x2="0" y2="1">
          <stop offset="0" stop-color="var(--bronze-light)"/>
          <stop offset="1" stop-color="var(--bronze-dark)"/>
        </linearGradient>
        <filter id="lift" x="-10%" y="-10%" width="130%" height="130%">
          <feDropShadow dx="10" dy="10" stdDeviation="6" flood-color="#000" flood-opacity=".35"/>
        </filter>
      </defs>
      <g transform="rotate(-10.5 408 423)">
        <text x="110" y="535" font-size="300" textLength="600" lengthAdjust="spacingAndGlyphs" filter="url(#lift)">
          <tspan fill="url(#bronze)">D</tspan><tspan fill="rgba(255,255,255,.55)" stroke="var(--bronze-dark)" stroke-width="2">ANC</tspan><tspan fill="url(#bronze)">E</tspan>
        </text>
      </g>
    </svg>

    <div class="brand">
      <div class="brand-mark"></div>
      <div class="brand-name">LUMERA</div>
      <div class="brand-tagline">DANCE CENTER RIVERSIDE</div>
    </div>

    <ul class="class-list">
      <li><svg viewBox="0 0 14 18"><path d="M3 2l8 7-8 7" fill="none" stroke="currentColor" stroke-width="3"/></svg>Ballet</li>
      <li><svg viewBox="0 0 14 18"><path d="M3 2l8 7-8 7" fill="none" stroke="currentColor" stroke-width="3"/></svg>Contemporary Dance</li>
      <li><svg viewBox="0 0 14 18"><path d="M3 2l8 7-8 7" fill="none" stroke="currentColor" stroke-width="3"/></svg>High heels</li>
      <li><svg viewBox="0 0 14 18"><path d="M3 2l8 7-8 7" fill="none" stroke="currentColor" stroke-width="3"/></svg>Salsa &amp; Bachata &amp; Zouk</li>
      <li><svg viewBox="0 0 14 18"><path d="M3 2l8 7-8 7" fill="none" stroke="currentColor" stroke-width="3"/></svg>Hip Hop</li>
    </ul>
  </main>
</body>
</html>
```